Business Card for a Life Coaching Company

BRAVOPEAK is a Life Coaching company that was initiated to support people who want to transform thier life or ana aspect of it.
our slogan is : "Dream. Believe. Succeed"
our logo is uploaded.
The name of the company implies that leadership, strength and wisdom required to change your life.
We want an attractive business card that would give an impression of reliability, support and change. so we really want it unique. Here are some examples of unique cards:

http://www.cardcraftvault.example/2009/05/100-really-creative-business-cards/

BravoPeak is a life coaching organization focusing on individual transformation through the application of relevant and timeless principles of success.  BravoPeak believes that real, sustainable life transformations are brought about by tuning into the timeless wisdom we each carry in our hearts while boldy acting in the direction of our dreams.

Contacts on the card:
Address: 7 Tarek Nour El Dine Heliopolis Cairo Egypt
Tel: +202 24 71 38 52
Fax: +202 24 71 38 17
Mobile: +2 012 684 2097 (Dalia Soliman)
+2 0199915815 (Tariq Bhatti)

By the way, our temporary website is http://www.bravopeak.example

We have attached an .eps file with various configurations of our logo.

```html
<!DOCTYPE html>
<html lang="en">
<head>
<meta charset="utf-8">
<title>BravoPeak Business Cards</title>
<link rel="stylesheet" href="https://fonts.googleapis.com/css2?family=Marcellus&family=Droid+Serif&family=Noto+Serif:wght@400&display=swap">
<style>
  :root {
    --page-bg: #e4e6e8;
    --card-bg-light: #fbfbf4;
    --card-bg-dark: #eaeadb;
    --brand-orange: #f15a22;
    --brand-peach: #f3a27f;
    --ink: #1d1d1b;
    --band-text: #ffffff;
  }
  * { margin: 0; padding: 0; box-sizing: border-box; }
  html, body {
    width: 1200px; height: 900px; overflow: hidden;
    background: var(--page-bg);
  }
  .business-card {
    position: absolute;
    left: 266px;
    width: 664px; height: 386px;
    overflow: hidden;
    background: linear-gradient(160deg, var(--card-bg-light) 0%, var(--card-bg-dark) 100%);
    box-shadow: 0 4px 14px rgba(0,0,0,0.28);
  }
  .card-front { top: 50px; }
  .card-back { top: 474px; }

  .mascot-art {
    position: absolute;
    left: 270px; top: -10px;
    width: 400px; height: 360px;
  }
  .card-front .mascot-art {
    background: radial-gradient(ellipse 60% 62% at 58% 48%, rgba(243,162,127,0.85) 0%, rgba(243,162,127,0.45) 55%, rgba(243,162,127,0) 100%);
  }
  .card-back .mascot-art {
    background: radial-gradient(ellipse 60% 62% at 58% 50%, rgba(241,90,34,0.9) 0%, rgba(241,90,34,0.45) 55%, rgba(241,90,34,0) 100%);
  }

  .brand-name {
    position: absolute;
    left: 24px; top: 16px;
    font-family: "Marcellus", serif;
    font-size: 46px;
    font-weight: 400;
    color: var(--brand-orange);
    letter-spacing: 1px;
  }

  .contact-block {
    position: absolute;
    left: 26px; top: 86px;
    font-family: "Droid Serif", "Noto Serif", serif;
    font-size: 20px;
    line-height: 25px;
    color: var(--ink);
  }
  .contact-group { margin-bottom: 12px; }
  .contact-label { color: var(--brand-orange); }
  .contact-group.mobile { margin-top: 20px; }

  .footer-band {
    position: absolute;
    left: 0; bottom: 0;
    width: 664px; height: 70px;
  }
  .footer-band path { fill: var(--brand-orange); }
  .site-url {
    position: absolute;
    left: 0; right: 0; bottom: 6px;
    text-align: center;
    font-family: "Noto Serif", serif;
    font-size: 35px;
    color: var(--band-text);
    letter-spacing: 0.5px;
  }

  .stacked-name {
    position: absolute;
    left: 28px; top: 92px;
    font-family: "Marcellus", serif;
    font-size: 70px;
    line-height: 78px;
    color: var(--ink);
  }
</style>
</head>
<body>

<section class="business-card card-front">
  <div class="mascot-art" role="img" aria-label="Stylised lion head illustration in soft peach tones"></div>
  <h1 class="brand-name">BRAVO PEAK</h1>
  <div class="contact-block">
    <div class="contact-group">
      <div class="contact-label">Address</div>
      <div>7 Tarek Nour El Dine</div>
      <div>Heliopolis Cairo Egypt</div>
    </div>
    <div class="contact-group">
      <div><span class="contact-label">Tel:</span> +202 24 71 38 52</div>
      <div><span class="contact-label">Fax:</span> +202 24 71 38 17</div>
    </div>
    <div class="contact-group mobile">
      <div class="contact-label">Mobile:</div>
      <div>+2 012 684 2097 (Dalia Soliman)</div>
      <div>+2 0197328406 (Tariq Bhatti)</div>
    </div>
  </div>
  <svg class="footer-band" viewBox="0 0 664 70" aria-hidden="true">
    <path d="M0 26 Q332 6 664 14 L664 70 L0 70 Z"/>
  </svg>
  <div class="site-url">www.BRAVOPEAK.com</div>
</section>

<section class="business-card card-back">
  <div class="mascot-art" role="img" aria-label="Stylised lion head illustration in bright orange"></div>
  <h2 class="stacked-name">BRAVO<br>PEAK</h2>
  <svg class="footer-band" viewBox="0 0 664 70" aria-hidden="true">
    <path d="M0 26 Q332 6 664 14 L664 70 L0 70 Z"/>
  </svg>
  <div class="site-url">www.BRAVOPEAK.com</div>
</section>

</body>
</html>
```